Stationery Design Project

We need a stationary design (business card, logo, letterhead) for a new company called "Meridel Kestrova".
We provide software and consulting services to improve business efficiency & increase team engagement.
We focus on workflow automation, business social networking software and collaboration and communication tools built on mobile platforms.
Updates

Target Market(s)

Business with multi-site,young, mobile workforces e.g Retailers, Hospitality

Industry/Entity Type

Communication

Requirements
Must have
• Letterhead to include;
Business Address: 17 Wendle St, Corvath Vale, TAS 7054
ABN : 48 615 207 392

```html
<!DOCTYPE html>
<html lang="en">
<head>
<meta charset="utf-8">
<title>Meridel Kestrova – Business Card</title>
<link rel="stylesheet" href="https://fonts.googleapis.com/css2?family=Oswald:wght@300;400&display=swap">
<style>
  :root {
    --brand-blue: #1a7cf7;
    --brand-grey: #7f7f7f;
    --paper: #ffffff;
    --backdrop: #f4f4f4;
    --card-edge: #2b2b2b;
  }
  * { margin: 0; padding: 0; box-sizing: border-box; }
  html, body {
    width: 1028px;
    height: 1200px;
    overflow: hidden;
    background: var(--backdrop);
    font-family: "Oswald", "Arial Narrow", sans-serif;
    font-weight: 300;
  }
  .card {
    position: absolute;
    left: 135px;
    width: 767px;
    height: 424px;
    background: var(--paper);
    border: 1px solid var(--card-edge);
    overflow: hidden;
    box-shadow: 0 10px 40px rgba(0,0,0,0.18);
  }
  .card--front { top: 120px; }
  .card--back { top: 661px; }
  .card__shapes {
    position: absolute;
    inset: 0;
    width: 100%;
    height: 100%;
  }
  .shape--blue { fill: var(--brand-blue); }
  .shape--grey { fill: var(--brand-grey); stroke: var(--paper); stroke-width: 6; }

  .brand {
    position: absolute;
    left: 34px;
    top: 52px;
    display: flex;
    align-items: center;
    gap: 14px;
  }
  .brand__square {
    width: 34px;
    height: 34px;
    background: var(--brand-blue);
  }
  .brand__name {
    font-size: 31px;
    font-weight: 300;
    color: var(--brand-grey);
    letter-spacing: 0.5px;
    line-height: 1;
  }

  .person {
    position: absolute;
    left: 38px;
    top: 214px;
  }
  .person__name {
    font-size: 27px;
    font-weight: 400;
    color: var(--brand-blue);
    line-height: 1.1;
  }
  .person__role {
    font-size: 21px;
    color: var(--brand-grey);
    line-height: 1.4;
    margin-bottom: 12px;
  }
  .contact { list-style: none; }
  .contact__row {
    display: flex;
    font-size: 23px;
    line-height: 32px;
    color: var(--brand-grey);
  }
  .contact__label {
    width: 32px;
    color: var(--brand-blue);
  }
  .contact__row--email { color: var(--brand-blue); }

  .address {
    position: absolute;
    left: 583px;
    top: 162px;
    width: 162px;
    text-align: center;
    font-style: normal;
    font-size: 23px;
    font-weight: 400;
    line-height: 32px;
    color: var(--paper);
  }

  .website {
    position: absolute;
    left: 240px;
    top: 176px;
    font-size: 46px;
    font-weight: 400;
    color: var(--brand-blue);
    line-height: 1.2;
  }
</style>
</head>
<body>

<section class="card card--front" aria-label="Business card front">
  <svg class="card__shapes" viewBox="0 0 767 424" aria-hidden="true">
    <polygon class="shape--blue" points="767,0 686,79 767,160"/>
    <polygon class="shape--blue" points="767,258 681,341 767,424"/>
    <polygon class="shape--grey" points="672,74 806,208 672,342 538,208"/>
  </svg>

  <div class="brand">
    <span class="brand__square"></span>
    <span class="brand__name">Meridel Kestrova</span>
  </div>

  <div class="person">
    <p class="person__name">Ansel Tarrow</p>
    <p class="person__role">Managing Director</p>
    <ul class="contact">
      <li class="contact__row"><span class="contact__label">T:</span><span>+61 2 8041 5527</span></li>
      <li class="contact__row"><span class="contact__label">M:</span><span>+61 455 302 118</span></li>
      <li class="contact__row contact__row--email"><span class="contact__label">E:</span><span>ansel.tarrow@meridelkestrova.com</span></li>
    </ul>
  </div>

  <address class="address">
    17 Wendle St<br>
    Corvath Vale<br>
    TAS 7054
  </address>
</section>

<section class="card card--back" aria-label="Business card back">
  <svg class="card__shapes" viewBox="0 0 767 424" aria-hidden="true">
    <polygon class="shape--blue" points="0,0 82,81 0,161"/>
    <polygon class="shape--blue" points="0,250 86,339 0,426"/>
    <polygon class="shape--grey" points="96,74 230,208 96,342 -38,208"/>
  </svg>
  <p class="website">www.meridelkestrova.com</p>
</section>

</body>
</html>
```